we need a retail ready label design for a 4 ct baking potato . must include U.S.#1 Golden Roasters product of the USA 4 ct 28 oz . packed by Mossy Hollow Farms Fernwick Vale using 3 colors ( earth tones )size will be 3 and one half inches long and 2 and one half inches wide . we are a produce packing company we wholesale to local supermarkets . these potatoes are packed in a black foam tray and overwrapped with a clear film , the label size will allow the potatoes to show thru the film , these are a russet baking potato brown in color . we need to play up Golden Roasters . all the other info can be kept small and on the bottom of the label . thank you.

```html
<!DOCTYPE html>
<html lang="en">
<head>
<meta charset="utf-8">
<title>Golden Roasters – U.S.#1 Baking Potato Label</title>
<link rel="stylesheet" href="https://fonts.googleapis.com/css2?family=Alfa+Slab+One&family=Raleway:wght@400&display=swap">
<style>
  :root {
    --straw: #e2d68c;
    --straw-light: #e6dc97;
    --mustard: #d8c75c;
    --cream: #f2ebc0;
    --bark: #4a3a2f;
    --clay: #9a7446;
  }
  html, body {
    margin: 0;
    padding: 0;
    overflow: hidden;
    background: var(--straw);
  }
  .label {
    position: relative;
    width: 857px;
    height: 1200px;
    overflow: hidden;
    background: var(--straw);
    font-family: "Raleway", sans-serif;
  }
  .label__art {
    position: absolute;
    inset: 0;
  }
  .origin-badge__text {
    position: absolute;
    left: 16px;
    top: 98px;
    margin: 0;
    color: var(--cream);
    font-size: 24px;
    line-height: 1.5;
  }
  .details {
    position: absolute;
    left: 0;
    right: 0;
    top: 1021px;
    margin: 0;
    text-align: center;
    color: var(--straw);
    font-size: 23px;
    line-height: 40px;
    letter-spacing: 0.3px;
  }
</style>
</head>
<body>
<main class="label">
  <svg class="label__art" width="857" height="1200" viewBox="0 0 857 1200">
    <!-- background stripes -->
    <rect class="stripe stripe--left" x="22" y="160" width="92" height="950" fill="#d9c963" opacity="0.9"/>
    <rect class="stripe stripe--highlight" x="148" y="160" width="28" height="950" fill="#f3ecbf" opacity="0.8"/>
    <rect class="stripe stripe--right" x="674" y="45" width="86" height="880" fill="#d8c75c"/>

    <!-- top band -->
    <path class="band band--top" d="M0 0H857V44C800 50 760 30 700 38C640 46 600 28 540 36C470 44 430 24 360 34C300 42 250 30 190 40C120 50 60 36 0 46Z" fill="var(--clay)"/>

    <!-- bottom band -->
    <rect class="divider" x="0" y="820" width="857" height="12" fill="var(--bark)"/>
    <rect class="band band--bottom" x="0" y="851" width="857" height="349" fill="var(--bark)"/>
    <path class="band band--ground" d="M0 1160C60 1150 120 1170 200 1152C280 1136 330 1160 400 1150C480 1140 540 1126 620 1148C700 1166 780 1140 857 1150V1200H0Z" fill="var(--clay)"/>
    <rect class="stripe stripe--glow" x="170" y="851" width="22" height="330" fill="#f3ecbf" opacity="0.25"/>

    <!-- decorative splash -->
    <rect class="splash" role="img" aria-label="Cream grunge splash ornament" x="42" y="995" width="44" height="150" rx="18" fill="var(--cream)"/>

    <!-- origin starburst -->
    <polygon class="origin-badge" fill="var(--bark)"
      points="0,58 30,48 58,60 82,46 108,62 138,52 152,78 182,86 170,112 196,130 176,152 188,180 160,190 166,220 136,214 122,240 100,220 74,238 60,212 30,226 22,198 0,206"/>

    <!-- emblem -->
    <circle class="emblem" cx="437" cy="572" r="366" fill="var(--straw-light)"/>
    <circle class="emblem__ring" cx="437" cy="572" r="328" fill="none" stroke="var(--bark)" stroke-width="17" stroke-dasharray="17 17"/>

    <text class="emblem__grade" x="437" y="440" text-anchor="middle" textLength="240" lengthAdjust="spacingAndGlyphs"
      font-family="'Alfa Slab One', serif" font-size="74" fill="var(--bark)">U.S.#1</text>
    <text class="emblem__name" x="437" y="606" text-anchor="middle" textLength="580" lengthAdjust="spacingAndGlyphs"
      font-family="'Alfa Slab One', serif" font-size="118" fill="var(--straw-light)" stroke="var(--bark)" stroke-width="4">GOLDEN</text>
    <text class="emblem__name" x="437" y="731" text-anchor="middle" textLength="580" lengthAdjust="spacingAndGlyphs"
      font-family="'Alfa Slab One', serif" font-size="118" fill="var(--straw-light)" stroke="var(--bark)" stroke-width="4">ROASTERS</text>
  </svg>

  <p class="origin-badge__text">Product of<br>the USA</p>

  <p class="details">4 ct 28 oz<br>Packed by: Mossy Hollow Farms Fernwick Vale</p>
</main>
</body>
</html>
```